Book Cover Design

Design with title UNWAVERING
Subtitle: Ways to Kindle the Spark of Resolve
Author Name: Carla Jean Morrow
Put DAILY MERIDIAN BESTSELLER at top
Shimmer design, see inspirational images attached

```html
<!DOCTYPE html>
<html lang="en">
<head>
<meta charset="utf-8">
<title>Unwavering — Book Cover</title>
<link href="https://fonts.googleapis.com/css2?family=Bebas+Neue&display=swap" rel="stylesheet">
<style>
  :root {
    --page: #ffffff;
    --ink: #0b0b0b;
    --rim: #ffffff;
    --pink: #f7b3f3;
    --lilac: #d4c4f2;
    --periwinkle: #bfc6ef;
    --mint: #b7f1ec;
    --mist: #ece4f8;
  }
  * { margin: 0; padding: 0; box-sizing: border-box; }
  html, body {
    width: 935px;
    height: 1200px;
    overflow: hidden;
    background: var(--page);
  }
  .canvas {
    position: relative;
    width: 935px;
    height: 1200px;
  }
  .cover {
    position: absolute;
    left: 156px;
    top: 133px;
    width: 624px;
    height: 936px;
    overflow: hidden;
    font-family: "Bebas Neue", "Oswald", sans-serif;
    color: var(--ink);
    text-align: center;
  }
  .cover__wash {
    position: absolute;
    inset: 0;
    background:
      radial-gradient(ellipse 55% 40% at 10% 85%, var(--pink) 0%, transparent 70%),
      radial-gradient(ellipse 45% 35% at 5% 50%, var(--pink) 0%, transparent 70%),
      radial-gradient(ellipse 50% 30% at 45% 45%, var(--mist) 0%, transparent 70%),
      radial-gradient(ellipse 60% 45% at 95% 20%, var(--mint) 0%, transparent 75%),
      radial-gradient(ellipse 40% 35% at 90% 60%, var(--mint) 0%, transparent 75%),
      radial-gradient(ellipse 50% 40% at 75% 95%, var(--periwinkle) 0%, transparent 75%),
      linear-gradient(125deg, var(--lilac) 0%, var(--lilac) 35%, var(--periwinkle) 55%, var(--mint) 80%);
  }
  .cover__badge {
    position: absolute;
    top: 30px;
    left: 0;
    right: 0;
    font-size: 48px;
    line-height: 1;
    letter-spacing: 0.5px;
  }
  .cover__author {
    position: absolute;
    top: 91px;
    left: 0;
    right: 0;
    font-size: 37px;
    line-height: 1;
    letter-spacing: 1px;
  }
  .cover__title {
    position: absolute;
    left: 56px;
    top: 380px;
    width: 520px;
    height: 120px;
    overflow: visible;
  }
  .cover__title text {
    font-family: "Bebas Neue", "Oswald", sans-serif;
    font-size: 140px;
    fill: var(--ink);
    stroke: var(--rim);
    stroke-width: 3px;
    paint-order: stroke;
  }
  .cover__subtitle {
    position: absolute;
    top: 518px;
    left: 0;
    right: 0;
    font-size: 38px;
    line-height: 1;
    letter-spacing: 1px;
  }
</style>
</head>
<body>
  <div class="canvas">
    <div class="cover">
      <div class="cover__wash" role="img" aria-label="Soft watercolour wash in pink, lilac and mint"></div>
      <p class="cover__badge">DAILY MERIDIAN BEST SELLER</p>
      <p class="cover__author">CARLA JEAN MORROW</p>
      <svg class="cover__title" viewBox="0 0 520 120" aria-label="UNWAVERING">
        <text class="cover__title-shadow" x="5" y="106" textLength="490" lengthAdjust="spacingAndGlyphs">UNWAVERING</text>
        <text class="cover__title-face" x="17" y="112" textLength="490" lengthAdjust="spacingAndGlyphs">UNWAVERING</text>
      </svg>
      <p class="cover__subtitle">WAYS TO KINDLE THE SPARK OF RESOLVE</p>
    </div>
  </div>
</body>
</html>
```